Website for legal expungement services with button to qualify/disqualify potential clients

Larkfield Record Relief, LLC is a law firm focusing in legal expungement servcies (allowing people to erase criminal court records, police records, proseution files, etc). I want a more modern look which exudes confidence in the services. I am looking for a clean website that looks very polished. I want to keep the pages to a minimum, as I want the page not so much to answer questions, but to direct traffic to contact the law office. I would like the main focus point to be an button which would take a client through a series of questions to see if they would qualify for the services; this serves two purposes 1) to collect contact info for future marketing via email and 2) eliminate individuals who we are currently unable to help. A current theme that I have played around with are "Change so much, you'll need to reintroduce yourself" alongside a picture of a guys hand outstretched.
On the landing page, I would like a very brief and to the point explanation of what the service would be (i.e. "Leave your past in the past; expunge all your criminal records" ), followed by a list of benefits that it provides. (NB: included is a file "law post card-02" that includes the main benefits to expungement). Also included are two logo files for a more updated logo I currently use ("LRR Logo" and LRR Logo2") (NB: I'm open to revisions on this as well). Lastly, I've had two very minor 'ads' that I did ("postcard back" and "HVC Ad") that I like the idea of.

Target Market(s)

Middle/upper-middle class, mostly male, people with a criminal record or criminal accusation

Industry/Entity Type

Legal Services

Coding

Coded - Design and coding required

Requirements
Must have
• Button that attracts attention up front (possibly stand out coloring) to click to open up a series of questions to qualify/eliminate prospects, and simultaneously gather their info. Also, must be mobile friendly.

```html
<!DOCTYPE html>
<html lang="en">
<head>
<meta charset="utf-8">
<title>Eligibility Form – Larkfield Record Relief</title>
<link href="https://fonts.googleapis.com/css2?family=Marcellus+SC&family=Questrial&display=swap" rel="stylesheet">
<style>
:root{
  --navy:#0d3b77;
  --footer:#003a70;
  --bar:#333333;
  --ink:#333333;
  --line:#e3e3e3;
  --notice-bg:#eef5fd;
  --white:#ffffff;
}
*{box-sizing:border-box;margin:0;padding:0}
html,body{width:1200px;height:1006px;overflow:hidden;background:var(--white)}
body{position:relative;font-family:"Questrial",sans-serif;color:var(--ink)}
.site-header{position:absolute;left:0;top:0;width:1200px;height:116px;border-bottom:1px solid var(--line);display:flex;align-items:center;justify-content:center}
.brand{display:flex;align-items:center;gap:12px;font-family:"Marcellus SC",serif;color:var(--navy);font-size:20px;line-height:20px;letter-spacing:.5px}
.brand-mark{width:16px;height:16px;background:var(--navy)}
.page-title{position:absolute;top:170px;left:0;width:1200px;text-align:center;font-family:"Marcellus SC",serif;font-size:44px;color:var(--navy);font-weight:400;letter-spacing:1px}
.question{position:absolute;left:161px;width:890px;font-family:"Marcellus SC",serif;font-size:16.5px;color:var(--navy);letter-spacing:.8px;line-height:22px;font-weight:400}
.question .num{display:inline-block;width:16px}
.question .wrap{padding-left:16px;display:block}
.options{position:absolute;left:161px;display:flex;gap:22px;font-size:13px;color:var(--ink);align-items:center}
.option{display:flex;align-items:center;gap:9px}
.radio{width:9px;height:9px;border:1.4px solid #444;border-radius:50%;position:relative}
.radio.checked{border-color:var(--navy)}
.radio.checked::after{content:"";position:absolute;left:1.2px;top:1.2px;width:4px;height:4px;border-radius:50%;background:var(--navy)}
.options sup{font-size:7px;margin-right:1px}
.notice{position:absolute;left:161px;top:566px;width:878px;height:105px;border:1px solid var(--navy);border-radius:10px;background:linear-gradient(90deg,#f3f8fe,var(--notice-bg));padding:19px 24px;font-size:12.3px;line-height:24.5px;color:var(--ink)}
.notice a{color:var(--navy);font-weight:700;text-decoration:none}
.site-footer{position:absolute;left:0;top:762px;width:1200px;height:199px;background:var(--footer);color:var(--white)}
.footer-brand{position:absolute;left:398px;top:62px;color:var(--white)}
.footer-brand .brand-mark{background:var(--white)}
.footer-brand.brand{font-size:15px}
.secure-badge{position:absolute;left:671px;top:41px;width:132px;height:55px;border-radius:6px;background:#e9e9e9;border:2px solid #bbb}
.secure-badge::after{content:"";position:absolute;right:3px;top:3px;width:42px;height:45px;border-radius:3px;background:#9cc13a}
.contact{position:absolute;top:131px;display:flex;align-items:center;gap:13px;font-size:14.5px;line-height:22px}
.contact .icon{width:38px;height:38px;border:1.5px solid var(--white);border-radius:50%;display:flex;align-items:center;justify-content:center}
.contact strong{font-weight:700;display:block}
.bottom-bar{position:absolute;left:0;top:961px;width:1200px;height:45px;background:var(--bar);color:var(--white);font-size:13px}
.bottom-bar p{position:absolute;left:163px;top:14px}
.social{position:absolute;top:10px;width:26px;height:26px;border:1.3px solid var(--white);border-radius:50%}
</style>
</head>
<body>
<header class="site-header">
  <div class="brand"><span class="brand-mark"></span><span>Larkfield Record Relief</span></div>
</header>

<main>
  <h1 class="page-title">Eligibility Form</h1>

  <h2 class="question" style="top:258px"><span class="num">1.</span>Are you trying to expunge a case that resulted in a conviction?</h2>
  <div class="options" style="top:291px">
    <label class="option"><span class="radio checked"></span>Yes</label>
    <label class="option"><span class="radio"></span>No</label>
  </div>

  <h2 class="question" style="top:325px"><span class="num">2.</span>What level of crime did you take a plea to?</h2>
  <div class="options" style="top:358px">
    <label class="option"><span class="radio checked"></span>Any crime involving domestic violence</label>
    <label class="option"><span class="radio"></span>4<sup>th</sup> deg felony</label>
    <label class="option"><span class="radio"></span>3<sup>rd</sup> deg felony</label>
    <label class="option"><span class="radio"></span>2<sup>nd</sup> deg felony</label>
    <label class="option"><span class="radio"></span>1<sup>st</sup> deg felony</label>
  </div>

  <h2 class="question" style="top:393px;width:900px"><span class="num">3.</span>Has it been at least ten years since you've been on parole/probation (for this or any other case):</h2>
  <div class="options" style="top:426px">
    <label class="option"><span class="radio checked"></span>Yes</label>
    <label class="option"><span class="radio"></span>No</label>
  </div>

  <h2 class="question" style="top:460px"><span class="num">4.</span>Did your case involve any of the following: A crime against a child, great bodily harm, any sex <span class="wrap">offense, embezzlement, or a DWI?</span></h2>
  <div class="options" style="top:516px">
    <label class="option"><span class="radio checked"></span>Yes</label>
    <label class="option"><span class="radio"></span>No</label>
  </div>

  <div class="notice">Based on the information provided, your case may not be eligible at this time; however, you may be eligible at a later date. If you'd like more details regarding eligibility or to get a more personalized review, you can reach out to our office by phone at <a href="tel:5055550143">505-555-0143</a> and an attorney will be able to make a full legal determination for you at no cost.</div>
</main>

<footer class="site-footer">
  <div class="brand footer-brand"><span class="brand-mark"></span><span>Larkfield Record Relief</span></div>
  <div class="secure-badge" role="img" aria-label="Secure connection badge"></div>

  <div class="contact" style="left:241px">
    <span class="icon"><svg width="14" height="18" viewBox="0 0 14 18"><path d="M7 0C3.1 0 0 3 0 6.8 0 11.5 7 18 7 18s7-6.5 7-11.2C14 3 10.9 0 7 0z" fill="#fff"/><circle cx="7" cy="6.8" r="2.6" fill="#003a70"/></svg></span>
    <span>2400 Cedar Row NW, Suite B,<br>Larkfield, NM 87190</span>
  </div>
  <div class="contact" style="left:528px">
    <span class="icon"><svg width="18" height="18" viewBox="0 0 24 24"><path d="M6.6 10.8a15 15 0 0 0 6.6 6.6l2.2-2.2c.3-.3.7-.4 1-.2 1.1.4 2.3.6 3.6.6.6 0 1 .4 1 1V20c0 .6-.4 1-1 1A17 17 0 0 1 3 4c0-.6.4-1 1-1h3.5c.6 0 1 .4 1 1 0 1.3.2 2.5.6 3.6.1.3 0 .7-.2 1z" fill="#fff"/></svg></span>
    <span><strong>Phone</strong>505-555-0143</span>
  </div>
  <div class="contact" style="left:754px">
    <span class="icon"><svg width="18" height="13" viewBox="0 0 18 13"><rect width="18" height="13" rx="1" fill="#fff"/><path d="M1 1l8 6 8-6M1 12l6-5M17 12l-6-5" stroke="#003a70" stroke-width="1.2" fill="none"/></svg></span>
    <span><strong>Email</strong>intake@halvorsenlaw.com</span>
  </div>
</footer>

<div class="bottom-bar">
  <p>(C) 2023 Larkfield Record Relief, LLC is a subsidiary of Halvorsen Law Group, LLC.All rights reserved.</p>
  <span class="social" style="left:978px"></span>
  <span class="social" style="left:1013px"></span>
</div>
</body>
</html>
```